Psychologist in Private Practice Needs a Website Update

Project Description:
Hello talented designers! My current website, www.jodelbrisk.com, needs a fresh, boho-modern makeover that highlights the warm, welcoming nature of my holistic therapy practice. I want a website that has a serene, boho- modern design, appealing to clients seeking individual therapy, couples therapy, and family counseling.

I’d also like to prepare for a future second site focused exclusively on couples and family therapy. Both sites should be interconnected, so I’m looking for design suggestions that seamlessly link them together while maintaining a cohesive brand look and feel.

Key Objectives:

Boho-Modern Aesthetic: Incorporate natural textures, neutral or earthy tones, and clean lines that capture a modern, inviting vibe.

Responsive Design: Ensure the website is user-friendly on desktop, tablet, and mobile devices.

Clear Service Offerings: Prominently feature my three distinct services: individual therapy, couples therapy, and family counseling.

Interlinked Future Site: Provide ideas on how to cross-link this site with a second site focused on couples and family therapy.

User Experience (UX): Make the site simple to navigate, with intuitive placement of content that speaks to potential clients’ needs.

SEO-Friendly: Implement best practices for structure, site speed, and keyword usage to boost online visibility.

What I Have Now:
Existing website: www.jodelbrisk.com
Basic content and a logo that can be refined or updated to match the boho-modern feel
Rough style guide with brand elements open to a fresh interpretation

Preferred Style/Tone:
Boho-modern with earthy tones, subtle textures, and clean typography
Warm, empathetic, and approachable to align with the nature of therapy services
Slightly artistic or organic elements that evoke calm and connection

Potential for an ongoing design relationship!
Updates

Need extra days to review

Target Market(s)

I have a high functioning, professional clientele who doctors, lawyers, and leaders in their field.

Industry/Entity Type

healthcare/mental health

Coding

Coded - Design and coding required

Font styles to use
Other font styles liked:
• cormorant garamond for headers and Source Sans Pro for supporting text

Colors

Designer to choose colors to be used in the design.

Requirements
Must have
• Open, Harmonious Layout I’d like the overall design to feel upscale, humanistic, open and harmonious, with minimal divisions of space. Rather than traditional section dividers, please consider using images, subtle shifts in color, typography, or spacing to define sections. Hero Image & Inspiration Ideally, the first (hero) image should evoke a sense of awe or inspiration. Focus on simplicity and elegance so the design feels spacious and inviting, allowing the content and imagery to really stand out. Natural Flow Wherever possible, let the design elements flow naturally into each other, creating a sense of unity and cohesion throughout the site.
Nice to have
• 1. Full-Width Hero Image: • The homepage should feature a full-width hero image that extends edge-to-edge across the screen for a modern and visually immersive effect. • This image should set the tone for the website, reflecting a calming, humanistic/natural, and upscale feel. It could include subtle overlays or gradients to enhance readability of text and navigation elements. Ideally, this image should have one or two people in nature. The image could be slightly transparent to allow the text "holistic therapy" and the tagline "an integrative approach to transformation" to be easily visible. Please help me find a breath-taking image that evokes a sense of beauty, inspiration, awe or hope. 2. Menu Tabs Positioned Over the Image: • The menu tabs (navigation bar) should be positioned directly on top of the hero image, either centered or aligned to the top right/left, depending on the design. • The navigation bar should have a slightly transparent or solid background (depending on the image and visibility needs) to ensure the text is easily readable without detracting from the image. 3. Typography and Text Placement: • The text overlay on the hero image should use the selected fonts: • Cormorant Garamond for headers (e.g., the tagline or welcome message). • Source Sans Pro for any supporting text. 5. Seamless Transitions: • Below the full-width image, transitions into the next sections (like “About,” “Services,” or client-focused content) should be smooth, using full-width separators that maintain the cohesive, open layout style. 6. Color Palette: • A neutral and calming color palette should be used (e.g., soft blues, grays, whites, or very muted earth tones) to create a soothing atmosphere for visitors. This design approach ensures the homepage looks clean, modern, and professional while maintaining the calming and upscale aesthetic that reflects the values of my psychology practice

```html
<!DOCTYPE html>
<html lang="en">
<head>
<meta charset="utf-8">
<title>Dr. Lena Marwick — Holistic Therapy</title>
<link href="https://fonts.googleapis.com/css2?family=Gloock&family=Tinos:wght@400;700&family=Poppins:wght@400;500&display=swap" rel="stylesheet">
<style>
:root{
  --cream:#f6f0e7;
  --cream-2:#f9f5ef;
  --sand:#efebe6;
  --brown:#6a3f12;
  --brown-card:#a05f1d;
  --orange:#c9771f;
  --orange-light:#e2a765;
  --ink:#2b2220;
  --muted:#4a403a;
  --footer:#2c221c;
  --white:#ffffff;
}
*{box-sizing:border-box;margin:0;padding:0}
html,body{width:1200px;height:5333px;overflow:hidden}
body{font-family:"Tinos",serif;color:var(--ink);background:var(--white);position:relative}
.display{font-family:"Gloock",serif;font-weight:400}
.btn{display:inline-flex;align-items:center;justify-content:center;background:var(--orange);color:var(--white);border-radius:20px;font-size:14px;height:37px;padding:0 28px;text-decoration:none}
.eyebrow{color:var(--orange);font-size:20px}
section,header,footer{position:absolute;left:0;width:1200px}
.abs{position:absolute}
.photo{background:linear-gradient(135deg,#d9b48c,#8a6a4c)}

/* header */
.site-header{top:0;height:68px;background:var(--cream);border-bottom:1px solid #ece2d4}
.brand{position:absolute;left:66px;top:10px;display:flex;align-items:center;gap:10px;font-family:"Poppins",sans-serif}
.brand-dot{width:46px;height:46px;border-radius:50%;background:var(--orange)}
.brand-name{font-size:20px;line-height:1;color:var(--ink)}
.brand-sub{font-size:14px;color:var(--ink);margin-top:3px}
.nav{position:absolute;top:24px;left:0;font-size:15px}
.nav a{position:absolute;white-space:nowrap;color:var(--ink);text-decoration:none}
.nav a.active{color:var(--orange)}
.header-cta{position:absolute;left:941px;top:14px;width:191px;height:38px;padding:0}

/* hero */
.hero{top:68px;height:687px;background:var(--cream);overflow:hidden}
.hero h1{position:absolute;left:66px;top:220px;font-size:72px;color:var(--ink)}
.hero p{position:absolute;left:66px;top:328px;width:540px;font-size:19px;line-height:30px;color:var(--muted)}
.hero .btn{position:absolute;left:66px;top:414px;width:141px;padding:0;height:36px}
.hero-photo{position:absolute;left:612px;top:4px;width:588px;height:683px;border-radius:294px 294px 0 0;background:linear-gradient(160deg,#9bb26a,#d6c08f 45%,#e6a7b5 80%)}
.hero-rings{position:absolute;left:560px;top:430px}

/* offerings */
.offerings{top:755px;height:797px;background:var(--brown);color:var(--cream)}
.offerings .eyebrow,.offerings h2,.offerings .lead{position:absolute;left:0;width:1200px;text-align:center}
.offerings .eyebrow{top:58px}
.offerings h2{top:92px;font-size:54px;color:var(--cream)}
.offerings .lead{top:168px;font-size:18px}
.offer{position:absolute;top:228px;width:342px}
.offer-frame{height:335px;background:var(--brown-card);padding:14px 12px}
.offer-frame .photo{height:253px}
.offer h3{margin-top:22px;font-size:28px;color:var(--cream)}
.offer p{margin-top:12px;font-size:13.5px;line-height:24px}
.offer .btn{margin-top:20px;width:137px;padding:0;height:38px}

/* welcome */
.welcome{top:1552px;height:451px;background:var(--white)}
.welcome-photo{position:absolute;left:0;top:0;width:445px;height:451px;background:linear-gradient(120deg,#b8651e,#e29e4a 60%,#f0c07a)}
.portrait{position:absolute;border:6px solid var(--white);border-radius:90px 90px 0 0;background:linear-gradient(170deg,#c9946b,#3c2a22)}
.welcome-text{position:absolute;left:520px;width:425px;top:88px;text-align:center}
.welcome-text h2{font-size:58px;margin-top:6px;color:var(--ink)}
.welcome-text .role{color:var(--orange);font-size:20px;margin-top:4px}
.welcome-text p{font-size:13.5px;line-height:23px;color:var(--muted);margin-top:12px}
.welcome-text .btn{margin-top:18px;width:139px;padding:0;height:38px}

/* specialist */
.specialist{top:2003px;height:697px;background:var(--white)}
.specialist .eyebrow,.specialist h2{position:absolute;left:0;width:1180px;text-align:center}
.specialist .eyebrow{top:88px}
.specialist h2{top:130px;font-size:54px}
.spec{position:absolute;width:240px}
.spec-icon{width:50px;height:50px;background:#a86a33;border-radius:3px;display:flex;align-items:center;justify-content:center}
.spec h3{font-size:23px;margin-top:14px;color:var(--ink)}
.spec p{font-size:13px;line-height:21px;color:var(--muted);margin-top:6px}
.spec p a{color:var(--orange);font-size:11px;text-decoration:none}

/* issues */
.issues{top:2700px;height:807px;background:var(--sand)}
.issue-arch{position:absolute;left:66px;top:89px;width:567px;height:629px;border-radius:284px 284px 0 0;background:var(--orange-light)}
.issue-photo{position:absolute;left:128px;top:155px;width:443px;height:563px;border-radius:222px 222px 0 0;background:linear-gradient(170deg,#c7b8a4,#5f7a4e 70%,#dacbb6)}
.issues-text{position:absolute;left:677px;top:150px;width:480px}
.issues-text h2{font-size:52px;line-height:64px;margin-top:14px}
.issues-text ul{list-style:none;margin-top:22px}
.issues-text li{font-size:13.5px;line-height:32px;color:var(--muted);display:flex;align-items:center;gap:8px}
.issues-text li::before{content:"";width:5px;height:5px;background:var(--orange)}
.issues-text .btn{margin-top:26px;width:138px;padding:0;height:38px}

/* communication */
.communication{top:3507px;height:735px;background:var(--white)}
.communication h2{position:absolute;top:100px;left:0;width:1200px;text-align:center;font-size:54px}
.comm-photo{position:absolute;left:66px;top:226px;width:617px;height:395px;background:linear-gradient(120deg,#e8e1da,#c7b4a0 55%,#f3efea)}
.comm-card{position:absolute;left:623px;top:310px;width:511px;height:311px;background:var(--brown);padding:62px 52px;color:var(--cream)}
.comm-card h3{font-size:28px;color:var(--cream)}
.comm-card h3 span{color:var(--orange)}
.comm-card p{font-size:13.5px;line-height:23px;margin-top:14px}
.comm-card .btn{margin-top:20px;width:138px;padding:0;height:38px}

/* faq */
.faq{top:4242px;height:686px;background:var(--cream-2)}
.faq h2{position:absolute;top:50px;left:0;width:1200px;text-align:center;font-size:54px}
.faq-list{position:absolute;left:213px;top:157px;width:772px;list-style:none}
.faq-list li{height:54.2px;display:flex;align-items:center;justify-content:space-between;border-bottom:1px solid #e6ddd0;font-size:19px;color:var(--muted)}
.faq-list li span.plus{width:30px;height:30px;border-radius:50%;border:1px solid #d9cbb8;color:var(--orange);display:flex;align-items:center;justify-content:center;font-size:16px}

/* footer */
.site-footer{top:4928px;height:405px;background:var(--footer);color:#d8cfc5}
.site-footer .brand{top:70px}
.site-footer .brand-name,.site-footer .brand-sub{color:var(--white)}
.footer-about{position:absolute;left:66px;top:136px;width:360px;font-size:13.5px;line-height:24px}
.socials{position:absolute;left:66px;top:242px;display:flex;gap:14px}
.socials span{width:30px;height:30px;border:1px solid #6a5a4c;display:block}
.footer-divider{position:absolute;top:40px;width:1px;height:300px;background:#43362c}
.footer-col{position:absolute;top:50px}
.footer-col h4{font-family:"Tinos",serif;font-weight:400;font-size:21px;color:var(--orange)}
.footer-col ul{list-style:none;margin-top:24px}
.footer-col li{font-size:14px;line-height:36px}
.contact-item{display:flex;gap:12px;align-items:flex-start;font-size:13.5px;line-height:21px}
.contact-icon{width:36px;height:36px;border-radius:50%;background:var(--orange);flex:none;display:flex;align-items:center;justify-content:center}
.copyright{position:absolute;bottom:22px;left:0;width:1200px;text-align:center;font-size:12px;color:#a79a8e;border-top:1px solid #43362c;padding-top:18px}
.copyright span{color:var(--orange)}
</style>
</head>
<body>

<header class="site-header">
  <div class="brand"><span class="brand-dot"></span><div><div class="brand-name">Dr. Lena Marwick</div><div class="brand-sub">Licensed Psychologist</div></div></div>
  <nav class="nav">
    <a class="active" style="left:453px">Home</a>
    <a style="left:532px">Services</a>
    <a style="left:624px">About</a>
    <a style="left:702px">FAQs</a>
    <a style="left:776px">Blog</a>
    <a style="left:844px">Contact Us</a>
  </nav>
  <a class="btn header-cta">Make An Appointment</a>
</header>

<section class="hero">
  <svg class="hero-rings" width="120" height="260" viewBox="0 0 120 260" aria-hidden="true">
    <g fill="none" stroke="#f0c9a2" stroke-width="4">
      <path d="M118 260V120a60 60 0 0 0-60-60"/><path d="M104 260V122a46 46 0 0 0-46-46"/><path d="M90 260V124a32 32 0 0 0-32-32"/>
    </g>
  </svg>
  <div class="hero-photo" role="img" aria-label="Woman in a pink cardigan resting her head on her hand with eyes closed, sitting outdoors among plants"></div>
  <h1 class="display">Holistic Theraphy</h1>
  <p>We offer therapy for individuals, couples and families to help you create meaningful change</p>
  <a class="btn">Explore More</a>
</section>

<section class="offerings">
  <div class="eyebrow">Clean Services</div>
  <h2 class="display">What We Offering</h2>
  <p class="lead">We offer therapy for individuals, couples and families to help you create meaningful change</p>
  <article class="offer" style="left:66px">
    <div class="offer-frame"><div class="photo" role="img" aria-label="Therapist in session with a young man on a sofa"></div></div>
    <h3 class="display">Individual Therapy</h3>
    <p>We work with adults (age 18+) using a highly personalized and flexible approach tailored to each...</p>
    <a class="btn">Read More</a>
  </article>
  <article class="offer" style="left:428px">
    <div class="offer-frame"><div class="photo" role="img" aria-label="Couple sitting on a sofa talking with a therapist"></div></div>
    <h3 class="display">Couples Therapy</h3>
    <p>We help couples understand how the distress in their relationship is caused by cycles of disconnection...</p>
    <a class="btn">Read More</a>
  </article>
  <article class="offer" style="left:792px">
    <div class="offer-frame"><div class="photo" role="img" aria-label="Family with a child in a counseling session"></div></div>
    <h3 class="display">Family Counseling</h3>
    <p>Relationships are the heart of the human experience. Instead of giving couples and families...</p>
    <a class="btn">Read More</a>
  </article>
</section>

<section class="welcome">
  <div class="welcome-photo" role="img" aria-label="Woman meditating cross-legged in a warm sunlit room"></div>
  <div class="portrait" style="left:335px;top:103px;width:174px;height:242px" role="img" aria-label="Portrait of the psychologist"></div>
  <div class="portrait" style="left:954px;top:101px;width:180px;height:247px;border:none" role="img" aria-label="Second portrait of the psychologist"></div>
  <div class="welcome-text">
    <div class="eyebrow">Welcome To</div>
    <h2 class="display">Dr Lena Marwick</h2>
    <div class="role">Owner, Licensed Clinical Psychologist</div>
    <p>I earned my Doctor of Psychology (Psy.D.) in Clinical Psychology from Harwell University of Westmark. In addition to my private practice in West Fernvale, WM</p>
    <a class="btn">Read More</a>
  </div>
</section>

<section class="specialist">
  <div class="eyebrow">Featured Services</div>
  <h2 class="display">Our Specialist</h2>
  <div class="spec" style="left:66px;top:236px"><div class="spec-icon"><svg width="28" height="28"><circle cx="14" cy="14" r="10" fill="none" stroke="#fff" stroke-width="2"/></svg></div><h3 class="display">Anxiety</h3><p>Anxiety may take many different forms, such as chronic worry, panic attacks, phobias... <a>Read More</a></p></div>
  <div class="spec" style="left:354px;top:236px"><div class="spec-icon"><svg width="28" height="28"><circle cx="14" cy="14" r="10" fill="none" stroke="#fff" stroke-width="2"/></svg></div><h3 class="display">Depression</h3><p>One of the most common reasons that people seek therapy, depression is often... <a>Read More</a></p></div>
  <div class="spec" style="left:621px;top:236px"><div class="spec-icon"><svg width="28" height="28"><circle cx="14" cy="14" r="10" fill="none" stroke="#fff" stroke-width="2"/></svg></div><h3 class="display">Dissatisfaction</h3><p>Chronic dissatisfaction or persistent low-grade depression pervades all aspects of life... <a>Read More</a></p></div>
  <div class="spec" style="left:906px;top:236px"><div class="spec-icon"><svg width="28" height="28"><circle cx="14" cy="14" r="10" fill="none" stroke="#fff" stroke-width="2"/></svg></div><h3 class="display">Relationships</h3><p>Everyone longs for connection and a sense of belonging, yet all too often we unintentionally... <a>Read More</a></p></div>
  <div class="spec" style="left:66px;top:436px"><div class="spec-icon"><svg width="28" height="28"><circle cx="14" cy="14" r="10" fill="none" stroke="#fff" stroke-width="2"/></svg></div><h3 class="display">Abuse</h3><p>Adults who were abused during childhood often have low self-esteem, tend to be more... <a>Read More</a></p></div>
  <div class="spec" style="left:354px;top:436px"><div class="spec-icon"><svg width="28" height="28"><circle cx="14" cy="14" r="10" fill="none" stroke="#fff" stroke-width="2"/></svg></div><h3 class="display">Grief</h3><p>Losing someone you love is one of the life's greatest sorrows. Feelings of grief can be... <a>Read More</a></p></div>
  <div class="spec" style="left:621px;top:436px"><div class="spec-icon"><svg width="28" height="28"><circle cx="14" cy="14" r="10" fill="none" stroke="#fff" stroke-width="2"/></svg></div><h3 class="display">Parenting</h3><p>There is a saying that a parent is only as happy as her least happy child. Having a child... <a>Read More</a></p></div>
  <div class="spec" style="left:906px;top:436px"><div class="spec-icon"><svg width="28" height="28"><circle cx="14" cy="14" r="10" fill="none" stroke="#fff" stroke-width="2"/></svg></div><h3 class="display">Food Allergies</h3><p>Parents of young children with severe food allergies can feel overwhelmed and fearful... <a>Read More</a></p></div>
</section>

<section class="issues">
  <div class="issue-arch"></div>
  <div class="issue-photo" role="img" aria-label="Woman in a green blouse meditating while a practitioner holds her head"></div>
  <div class="issues-text">
    <div class="eyebrow">Are you struggling with</div>
    <h2 class="display">Issues that affect the way you live love or work</h2>
    <ul>
      <li>Feel overwhelmed with depression or anxiety.</li>
      <li>Experience a lack of connection in your marriage.</li>
      <li>Worry excessively about what others think.</li>
      <li>Have a history of trauma or abuse.</li>
      <li>Parent a child with complex needs.</li>
      <li>Struggle with other life challenges.</li>
    </ul>
    <a class="btn">Read More</a>
  </div>
</section>

<section class="communication">
  <h2 class="display">Communication in Relationships</h2>
  <div class="comm-photo" role="img" aria-label="Smiling couple in white shirts relaxing on a sofa"></div>
  <div class="comm-card">
    <h3 class="display">Getting to the Heart <span>of the Issue</span></h3>
    <p>When couples say communication in relationships is their primary problem, they are missing opportunities to truly learn to understand each other.</p>
    <a class="btn">Read More</a>
  </div>
</section>

<section class="faq">
  <h2 class="display">Frequently Asked Question</h2>
  <ul class="faq-list">
    <li>Where are you located?<span class="plus">+</span></li>
    <li>What states do you offer telehealth in?<span class="plus">+</span></li>
    <li>What types of clients do you see?<span class="plus">+</span></li>
    <li>Do you take insurance?<span class="plus">+</span></li>
    <li>How do out of network benefits work?<span class="plus">+</span></li>
    <li>What can I expect in my first session?<span class="plus">+</span></li>
    <li>How many sessions do I need?<span class="plus">+</span></li>
    <li>What type of therapy do you do?<span class="plus">+</span></li>
    <li>What is EFT?<span class="plus">+</span></li>
  </ul>
</section>

<footer class="site-footer">
  <div class="brand"><span class="brand-dot"></span><div><div class="brand-name">Dr. Lena Marwick</div><div class="brand-sub">Licensed Psychologist</div></div></div>
  <p class="footer-about">We have extensive experience treating a full spectrum of mental health disorders using a collaborative and compassionate approach.</p>
  <div class="socials"><span></span><span></span><span></span></div>
  <div class="footer-divider" style="left:515px"></div>
  <div class="footer-divider" style="left:813px"></div>
  <div class="footer-col" style="left:621px">
    <h4>Quick Links</h4>
    <ul><li>Home</li><li>Services</li><li>About</li><li>FAQs</li><li>Blog</li><li>Contact Us</li></ul>
  </div>
  <div class="footer-col" style="left:892px">
    <h4>Contact Us</h4>
    <div style="margin-top:30px;display:flex;flex-direction:column;gap:28px">
      <div class="contact-item"><span class="contact-icon"><svg width="16" height="18" viewBox="0 0 16 18"><path d="M8 1a6 6 0 0 0-6 6c0 4.5 6 10 6 10s6-5.5 6-10a6 6 0 0 0-6-6z" fill="#fff"/><circle cx="8" cy="7" r="2" fill="#c9771f"/></svg></span><span>72 Lorem ipsum dolar sit amet<br>Fernvale 02KL, Westmark</span></div>
      <div class="contact-item" style="align-items:center"><span class="contact-icon"><svg width="16" height="16" viewBox="0 0 16 16"><path d="M3 1l3 3-1.5 2a9 9 0 0 0 5.5 5.5L12 10l3 3-2 2C7 15 1 9 1 3z" fill="#fff"/></svg></span><span>(555) 014-2290</span></div>
      <div class="contact-item" style="align-items:center"><span class="contact-icon"><svg width="16" height="12" viewBox="0 0 16 12"><rect x="0.5" y="0.5" width="15" height="11" fill="none" stroke="#fff"/><path d="M1 1l7 6 7-6" fill="none" stroke="#fff"/></svg></span><span>drlenamarwick@mailbox.com</span></div>
    </div>
  </div>
  <div class="copyright">© <span>Dr. Lena Marwick</span>, 2025. All Rights Reserved.</div>
</footer>

</body>
</html>
```